Graphic Design Set for Banner Ads - Sizes and Specs for Bidlane

We need a set of 6 ads of the following sizes created for Bidlane:

Medium rectangle: 300×250
Leaderboard: 728×90
Wide skyscraper: 160×600
Large rectangle: 300x600
Mobile leaderboard: 320×50

Here are the Formatting Guidelines (WEB ADS): https://help.bidlane.com/hc/en-us/articles/583920147-Ad-Content-and-Format-Guidelines

Here is the website: https://mavenhollowcare.com/

Here are some words for the ad - feel free to use creative liberties if you have something better or need less words.

1. The Future of Aging is Here

2. Dementia At-Home Care

3. Benefits of an Assisted Living from the Privacy of Your Home - link to

4. Idaho's New Senior Care Option

5. The Security of Senior Living from the Comfort of Your Home

I have the images for all website photos, if you need more images, please let me know.

Target Market(s)

Women age 55+

Industry/Entity Type

Graphic Design

Requirements
Must have
• Incorporate website imagery as much as possible
Should not have
• a feeling of helplessness, old, etc.

```html
<!DOCTYPE html>
<html lang="en">
<head>
<meta charset="utf-8">
<title>Maven Hollow – Dementia At-Home Care Banner Set</title>
<link href="https://fonts.googleapis.com/css2?family=Roboto:wght@400;500&display=swap" rel="stylesheet">
<style>
  :root {
    --canvas: #ece7e1;
    --ink: #222222;
    --gold: #b08a3c;
    --button: #0d0d0d;
    --button-text: #ffffff;
    --panel: #f1f1f1;
    --panel-soft: #e4e4e4;
    --photo-light: #e3ead9;
    --photo-mid: #c9d4bd;
    --photo-dark: #2a2f33;
  }
  * { box-sizing: border-box; margin: 0; padding: 0; }
  html, body { width: 1200px; height: 1075px; overflow: hidden; }
  body {
    background: var(--canvas);
    font-family: "Roboto", Arial, sans-serif;
    color: var(--ink);
    position: relative;
  }
  .ad { position: absolute; overflow: hidden; background: var(--panel); }
  .photo {
    position: absolute;
    background: linear-gradient(160deg, var(--photo-light) 0%, var(--photo-mid) 55%, var(--photo-dark) 100%);
  }
  .headline { font-weight: 500; color: var(--ink); line-height: 1; }
  .subline { font-weight: 400; color: var(--gold); line-height: 1; letter-spacing: 0.01em; }
  .cta {
    position: absolute;
    background: var(--button);
    color: var(--button-text);
    font-weight: 400;
    display: flex; align-items: center; justify-content: center;
    letter-spacing: 0.04em;
    white-space: nowrap;
  }
  .brand {
    position: absolute;
    display: flex; align-items: center; gap: 6px;
    font-weight: 400; color: var(--ink); letter-spacing: 0.04em; white-space: nowrap;
  }
  .brand-dot { border-radius: 50%; background: var(--gold); flex: none; }
  .brand-panel { display: flex; align-items: center; justify-content: center; }
  .brand-panel .brand { position: static; }

  /* Leaderboard 728×90 */
  .leaderboard { left: 78px; top: 75px; width: 907px; height: 112px;
    background: linear-gradient(90deg, var(--photo-mid), var(--photo-light)); }
  .leaderboard .photo { left: 0; top: 0; width: 172px; height: 112px; }
  .leaderboard .copy { position: absolute; left: 187px; top: 38px; display: flex; align-items: baseline; gap: 10px; }
  .leaderboard .headline { font-size: 30px; }
  .leaderboard .subline { font-size: 28px; }
  .leaderboard .cta { left: 572px; top: 37px; width: 150px; height: 37px; font-size: 15px; }
  .leaderboard .brand-panel { position: absolute; left: 745px; top: 0; width: 162px; height: 112px; background: var(--panel); }
  .leaderboard .brand { font-size: 15px; gap: 5px; letter-spacing: 0.02em; }
  .leaderboard .brand-dot { width: 9px; height: 9px; }

  /* Large rectangle 300×600 */
  .large-rect { left: 78px; top: 240px; width: 374px; height: 747px; }
  .large-rect .photo { left: 0; top: 0; width: 374px; height: 422px; }
  .large-rect .copy-panel { position: absolute; left: 0; top: 422px; width: 374px; height: 233px;
    background: linear-gradient(180deg, var(--panel) 0%, var(--panel-soft) 100%); text-align: center; }
  .large-rect .headline { margin-top: 22px; font-size: 54px; }
  .large-rect .subline { margin-top: 14px; font-size: 32px; }
  .large-rect .cta { left: 100px; top: 150px; width: 175px; height: 50px; font-size: 17px; }
  .large-rect .brand { left: 50%; transform: translateX(-50%); top: 690px; font-size: 28px; }
  .large-rect .brand-dot { width: 14px; height: 14px; }

  /* Wide skyscraper 160×600 */
  .skyscraper { left: 500px; top: 240px; width: 200px; height: 747px; }
  .skyscraper .photo { left: 0; top: 0; width: 200px; height: 247px; }
  .skyscraper .copy-panel { position: absolute; left: 0; top: 247px; width: 200px; height: 353px;
    background: linear-gradient(180deg, var(--panel) 0%, var(--panel-soft) 100%); text-align: center; }
  .skyscraper .headline { margin-top: 25px; font-size: 32px; }
  .skyscraper .subline { margin-top: 12px; font-size: 23px; }
  .skyscraper .cta { left: 26px; top: 125px; width: 150px; height: 37px; font-size: 15px; }
  .skyscraper .brand { left: 50%; transform: translateX(-50%); top: 668px; font-size: 17px; }
  .skyscraper .brand-dot { width: 10px; height: 10px; }

  /* Medium rectangle 300×250 */
  .medium-rect { left: 750px; top: 240px; width: 375px; height: 310px; }
  .medium-rect .photo { left: 0; top: 0; width: 375px; height: 247px;
    background: linear-gradient(100deg, var(--photo-dark) 0%, var(--photo-mid) 45%, var(--photo-light) 100%); }
  .medium-rect .copy { position: absolute; right: 14px; top: 50px; text-align: right; }
  .medium-rect .headline { font-size: 32px; }
  .medium-rect .subline { margin-top: 8px; font-size: 22px; }
  .medium-rect .brand { left: 20px; top: 270px; font-size: 17px; }
  .medium-rect .brand-dot { width: 10px; height: 10px; }
  .medium-rect .cta { left: 200px; top: 263px; width: 150px; height: 37px; font-size: 15px; }

  /* Mobile leaderboard 320×50 */
  .mobile-leaderboard { left: 750px; top: 602px; width: 400px; height: 62px;
    background: linear-gradient(90deg, var(--photo-mid), var(--photo-light)); }
  .mobile-leaderboard .photo { left: 0; top: 0; width: 80px; height: 62px; }
  .mobile-leaderboard .copy { position: absolute; left: 86px; top: 12px; text-align: center; }
  .mobile-leaderboard .headline { font-size: 18px; }
  .mobile-leaderboard .subline { margin-top: 5px; font-size: 12px; }
  .mobile-leaderboard .cta { left: 188px; top: 19px; width: 102px; height: 24px; font-size: 10px; }
  .mobile-leaderboard .brand-panel { position: absolute; left: 300px; top: 0; width: 100px; height: 62px; background: var(--panel); }
  .mobile-leaderboard .brand { font-size: 9px; gap: 3px; letter-spacing: 0.01em; }
  .mobile-leaderboard .brand-dot { width: 5px; height: 5px; }
</style>
</head>
<body>

  <section class="ad leaderboard">
    <div class="photo" role="img" aria-label="Photo of a senior gentleman resting his hands on a cane"></div>
    <div class="copy"><span class="headline">Dementia</span><span class="subline">AT-HOME CARE</span></div>
    <div class="cta">LEARN MORE</div>
    <div class="brand-panel"><div class="brand"><span class="brand-dot"></span>MAVEN HOLLOW</div></div>
  </section>

  <section class="ad large-rect">
    <div class="photo" role="img" aria-label="Portrait of a senior gentleman resting his hands on a cane"></div>
    <div class="copy-panel">
      <div class="headline">Dementia</div>
      <div class="subline">AT-HOME CARE</div>
      <div class="cta">LEARN MORE</div>
    </div>
    <div class="brand"><span class="brand-dot"></span>MAVEN HOLLOW</div>
  </section>

  <section class="ad skyscraper">
    <div class="photo" role="img" aria-label="Portrait of a senior gentleman resting his hands on a cane"></div>
    <div class="copy-panel">
      <div class="headline">Dementia</div>
      <div class="subline">AT-HOME CARE</div>
      <div class="cta">LEARN MORE</div>
    </div>
    <div class="brand"><span class="brand-dot"></span>MAVEN HOLLOW</div>
  </section>

  <section class="ad medium-rect">
    <div class="photo" role="img" aria-label="Senior gentleman seated on the left, resting his hands on a cane"></div>
    <div class="copy">
      <div class="headline">Dementia</div>
      <div class="subline">AT-HOME CARE</div>
    </div>
    <div class="brand"><span class="brand-dot"></span>MAVEN HOLLOW</div>
    <div class="cta">LEARN MORE</div>
  </section>

  <section class="ad mobile-leaderboard">
    <div class="photo" role="img" aria-label="Senior gentleman resting his hands on a cane"></div>
    <div class="copy">
      <div class="headline">Dementia</div>
      <div class="subline">AT-HOME CARE</div>
    </div>
    <div class="cta">LEARN MORE</div>
    <div class="brand-panel"><div class="brand"><span class="brand-dot"></span>MAVEN HOLLOW</div></div>
  </section>

</body>
</html>
```